flyer to promote aggregates company (special color aggregates)

We are existing one year and need more visibility.Therefor we are looking for a digital flyer, to be distributed to architects, study agencies, concrete and landscaping companies, etc.
Our job is to offer all special colored aggregates for the construction and landscaping industry to create new special worlds within an aesthetic aspect. Our speciality is to find quarries, logistics and organise the supply of different products within each project or supplier. More info on our website www.morvelstone.be (available in English).
The flyer should be class, modern and attractive. Idea is to invite to have a look on website and take on information with us. Imaging is central, a little text can be provided, in English, French and Dutch (we need these three languages, we can do the translations).
I have uploaded a previous home made brochure in English, which I used untill now to give around and promote our company... it is too much text. But gives other nice pictures. But I am not a specialist in that kind of things (made with MS Word).
Target Market(s)
architects, study engineering companies, precast concrete, concrete, landscaping and construction
Industry/Entity Type
Construction
Requirements
Must have
- - company logo
- - small part text
- - contact details !
- - pics

```html
<!DOCTYPE html>
<html lang="en">
<head>
<meta charset="utf-8">
<title>Morvel Stone – Flyer</title>
<link href="https://fonts.googleapis.com/css2?family=Oswald:wght@400;600;700&family=Open+Sans:wght@400;700&display=swap" rel="stylesheet">
<style>
  :root {
    --olive: #8b8f58;
    --olive-dark: #6f7343;
    --olive-light: #c7c98f;
    --olive-pale: #dfe0b8;
    --ink: #3a3a32;
    --paper: #ffffff;
    --backdrop: #ecebe6;
  }
  html, body {
    margin: 0;
    width: 1200px;
    height: 1000px;
    overflow: hidden;
    background: var(--backdrop);
  }
  .flyer {
    position: absolute;
    left: 50px;
    top: 130px;
    width: 1100px;
    height: 740px;
    background: var(--paper);
    box-shadow: 0 6px 24px rgba(0,0,0,.18);
    overflow: hidden;
    font-family: "Open Sans", Arial, sans-serif;
    color: var(--ink);
  }
  .flyer-shapes { position: absolute; inset: 0; }
  .brand {
    position: absolute;
    left: 40px;
    top: 34px;
    display: flex;
    align-items: center;
    gap: 14px;
  }
  .brand-square {
    width: 50px;
    height: 50px;
    background: var(--olive);
  }
  .brand-name {
    font-family: "Oswald", Arial, sans-serif;
    font-weight: 700;
    font-size: 46px;
    letter-spacing: 2px;
    color: var(--olive-dark);
    line-height: 1;
  }
  .intro, .services-text {
    position: absolute;
    left: 40px;
    width: 500px;
    font-size: 12.5px;
    line-height: 1.5;
    margin: 0;
  }
  .intro { top: 110px; }
  .intro strong, .services-text strong { color: var(--olive-dark); }
  .product-label {
    position: absolute;
    left: 40px;
    top: 214px;
    font-family: "Oswald", Arial, sans-serif;
    font-weight: 600;
    font-size: 15px;
    color: var(--olive-dark);
  }
  .product-grid {
    position: absolute;
    left: 120px;
    top: 210px;
    display: grid;
    grid-template-columns: repeat(3, 118px);
    grid-auto-rows: 88px;
    gap: 14px;
  }
  .product-tile { border-radius: 2px; }
  .tile-basalt  { background: linear-gradient(135deg, #2b2b2b, #4a4a48); }
  .tile-slate   { background: linear-gradient(135deg, #5a4a48, #8a7a74); }
  .tile-red     { background: linear-gradient(135deg, #8a3a22, #b0583a); }
  .tile-beige   { background: linear-gradient(135deg, #b89a70, #d8c4a0); }
  .tile-granite { background: linear-gradient(135deg, #6f6f6c, #a5a4a0); }
  .tile-yellow  { background: linear-gradient(135deg, #b4a676, #d6cda4); }
  .services-text { top: 420px; }
  .application-list {
    position: absolute;
    left: 40px;
    top: 500px;
    margin: 0;
    padding: 0;
    list-style: none;
    font-family: "Oswald", Arial, sans-serif;
    font-weight: 600;
    font-size: 20px;
    color: var(--olive-dark);
    line-height: 1.45;
  }
  .application-list li::before {
    content: "";
    display: inline-block;
    width: 0; height: 0;
    border-left: 6px solid transparent;
    border-right: 6px solid transparent;
    border-bottom: 10px solid var(--ink);
    margin-right: 14px;
    vertical-align: 2px;
  }
  .headline {
    position: absolute;
    left: 690px;
    top: 250px;
    font-family: "Oswald", Arial, sans-serif;
    line-height: .95;
    text-shadow: 0 2px 6px rgba(0,0,0,.35);
  }
  .headline-brand {
    display: block;
    font-size: 22px;
    font-weight: 400;
    letter-spacing: 1px;
    color: var(--olive-pale);
  }
  .headline-main {
    display: block;
    font-size: 82px;
    font-weight: 700;
    color: #fff;
  }
  .headline-sub {
    display: block;
    font-size: 52px;
    font-weight: 600;
    color: #fff;
    letter-spacing: 1px;
  }
  .contact-band {
    position: absolute;
    left: 0; right: 0; bottom: 0;
    height: 90px;
    display: flex;
    align-items: center;
    gap: 60px;
    padding-left: 40px;
    font-family: "Oswald", Arial, sans-serif;
    font-size: 30px;
    color: #fff;
    letter-spacing: 1px;
  }
</style>
</head>
<body>
  <div class="flyer">
    <svg class="flyer-shapes" width="1100" height="740" viewBox="0 0 1100 740">
      <defs>
        <linearGradient id="swoosh" x1="0" y1="0" x2="0" y2="1">
          <stop offset="0" stop-color="#dfe0b8"/>
          <stop offset="1" stop-color="#8b8f58"/>
        </linearGradient>
        <linearGradient id="scene" x1="0" y1="0" x2="1" y2="1">
          <stop offset="0" stop-color="#4f6a3a"/>
          <stop offset=".4" stop-color="#8a5a3c"/>
          <stop offset=".7" stop-color="#c9b48e"/>
          <stop offset="1" stop-color="#6fa6d6"/>
        </linearGradient>
        <linearGradient id="band" x1="0" y1="0" x2="0" y2="1">
          <stop offset="0" stop-color="#9a9e66"/>
          <stop offset="1" stop-color="#7c8049"/>
        </linearGradient>
        <clipPath id="upper"><rect x="0" y="0" width="1100" height="650"/></clipPath>
      </defs>
      <g clip-path="url(#upper)">
        <circle cx="1185" cy="330" r="610" fill="url(#swoosh)"/>
        <circle cx="1175" cy="330" r="582" fill="#a4a86e"/>
        <circle cx="1160" cy="330" r="560" fill="url(#scene)" role="img" aria-label="Photo collage of a quarry landscape and a garden bed of white gravel beside a pool"/>
      </g>
      <rect x="0" y="650" width="1100" height="90" fill="url(#band)"/>
    </svg>

    <div class="brand">
      <div class="brand-square"></div>
      <div class="brand-name">MORVEL STONE</div>
    </div>

    <p class="intro"><strong>Morvel Stone</strong> is a specialized trader of natural, synthetic and recycled aggregates throughout Europe. These sand and gravels are available for all applications of concrete, public works, road works and landscaping development.</p>

    <div class="product-label">PRODUCT:</div>
    <div class="product-grid">
      <div class="product-tile tile-basalt" role="img" aria-label="Black basalt gravel"></div>
      <div class="product-tile tile-slate" role="img" aria-label="Purple slate chippings"></div>
      <div class="product-tile tile-red" role="img" aria-label="Red crushed stone"></div>
      <div class="product-tile tile-beige" role="img" aria-label="Beige river pebbles"></div>
      <div class="product-tile tile-granite" role="img" aria-label="Grey granite chippings"></div>
      <div class="product-tile tile-yellow" role="img" aria-label="Yellow limestone gravel"></div>
    </div>

    <p class="services-text"><strong>Morvel Stone</strong> offers expertise and skills for the development of your project, from selection with attention to aesthetic and technical issues and challenges, to prescription, delivery during production and finishing the project. All this through our network of specialized partners.</p>

    <ul class="application-list">
      <li>CONCRETE</li>
      <li>ROAD BUILDING</li>
      <li>LANDSCAPING &amp; ARCHITECTURE</li>
    </ul>

    <h1 class="headline">
      <span class="headline-brand">MORVEL STONE</span>
      <span class="headline-main">CREATING</span>
      <span class="headline-sub">NEW WORLDS</span>
    </h1>

    <div class="contact-band">
      <span class="contact-phone">+32 (0)470 318 902</span>
      <span class="contact-web">www.morvelstone.be</span>
    </div>
  </div>
</body>
</html>
```